Business Card for Consulting Company

I would need a business card for my consulting company - the company brand and logos are defined and shared as part of this project. The proposed design for the business card can be reused as inspiration for my email signature.

```html
<!DOCTYPE html>
<html lang="en">
<head>
<meta charset="utf-8">
<title>Kinwell Advisory – Business Card</title>
<link rel="stylesheet" href="https://fonts.googleapis.com/css2?family=Open+Sans:wght@300;400;600;700&display=swap">
<style>
  :root {
    --bg: #dcd6d1;
    --teal: #149f9e;
    --teal-light: #2bb4b2;
    --teal-dark: #0f8c8b;
    --icon: #3f8b8a;
    --paper: #f4f4f4;
    --paper-shade: #e6e6e6;
    --ink: #1d1d1d;
    --white: #ffffff;
  }
  * { margin: 0; padding: 0; box-sizing: border-box; }
  html, body {
    width: 1200px; height: 960px; overflow: hidden;
    background: var(--bg);
    font-family: "Open Sans", sans-serif;
  }
  .canvas {
    width: 1200px; height: 960px;
    display: flex; flex-direction: column; align-items: center; justify-content: center;
    gap: 48px;
  }
  .card {
    width: 660px; height: 377px;
    border-radius: 3px;
    box-shadow: 0 10px 30px rgba(0,0,0,0.12);
    position: relative; overflow: hidden;
  }
  /* front */
  .card-front {
    background: linear-gradient(100deg, var(--teal-dark) 0%, var(--teal) 45%, var(--teal-light) 100%);
    display: flex; align-items: center; justify-content: center;
  }
  .brand {
    display: flex; align-items: center; gap: 18px;
    color: var(--white);
  }
  .brand-dot {
    width: 30px; height: 30px; border-radius: 50%;
    background: var(--white);
  }
  .brand-name {
    font-size: 58px; font-weight: 600; letter-spacing: 1px;
  }
  /* back */
  .card-back {
    background: linear-gradient(90deg, var(--paper) 0%, var(--paper) 50%, var(--paper-shade) 50.2%, var(--paper) 58%, var(--paper) 100%);
    display: grid; grid-template-columns: 1fr 1fr;
  }
  .holder {
    display: flex; flex-direction: column; justify-content: center;
    padding-left: 70px; padding-top: 20px;
    color: var(--ink);
  }
  .holder-name {
    font-size: 30px; font-weight: 300; letter-spacing: 0.5px; text-transform: uppercase;
  }
  .holder-name strong { font-weight: 700; }
  .holder-title {
    font-size: 17px; font-weight: 400; margin-top: 4px; padding-left: 70px;
  }
  .contacts {
    list-style: none;
    display: flex; flex-direction: column; justify-content: center; gap: 20px;
    padding-left: 28px;
  }
  .contact {
    display: flex; align-items: center; gap: 16px;
    font-size: 11px; font-weight: 600; line-height: 1.35;
    text-transform: uppercase; color: var(--ink);
  }
  .contact-icon {
    flex: none; width: 34px; height: 34px; border-radius: 50%;
    background: var(--icon);
    display: flex; align-items: center; justify-content: center;
  }
  .contact-icon svg { width: 18px; height: 18px; }
</style>
</head>
<body>
<main class="canvas">
  <section class="card card-front" aria-label="Card front">
    <div class="brand">
      <span class="brand-dot"></span>
      <span class="brand-name">Kinwell Advisory</span>
    </div>
  </section>

  <section class="card card-back" aria-label="Card back">
    <div class="holder">
      <p class="holder-name">Marlon <strong>Reyes</strong></p>
      <p class="holder-title">Senior Consultant</p>
    </div>
    <ul class="contacts">
      <li class="contact">
        <span class="contact-icon">
          <svg viewBox="0 0 20 20" fill="none" stroke="#fff" stroke-width="1.6"><rect x="2.5" y="5" width="15" height="10.5"/><path d="M2.5 5l7.5 6 7.5-6"/></svg>
        </span>
        <span>info@company-name</span>
      </li>
      <li class="contact">
        <span class="contact-icon">
          <svg viewBox="0 0 20 20" fill="#fff"><path d="M5.5 2.5l3 3-1.8 2c.9 2 2.6 3.7 4.6 4.6l2-1.8 3 3-2 2.2C9 15 5 11 3.3 4.5z"/></svg>
        </span>
        <span>+01 2345 6789 0123<br>+09 8765 4321 0987</span>
      </li>
      <li class="contact">
        <span class="contact-icon">
          <svg viewBox="0 0 20 20" fill="#fff"><path d="M10 3l7.5 7h-2.3v6.5h-3.7v-4.5h-3v4.5H4.8V10H2.5z"/></svg>
        </span>
        <span>Your city address<br>Street location, state, country</span>
      </li>
      <li class="contact">
        <span class="contact-icon">
          <svg viewBox="0 0 20 20" fill="none" stroke="#fff" stroke-width="1.5"><circle cx="10" cy="10" r="7"/><path d="M3 10h14M10 3c-3 3.5-3 10.5 0 14M10 3c3 3.5 3 10.5 0 14"/></svg>
        </span>
        <span>www.your-company-name</span>
      </li>
    </ul>
  </section>
</main>
</body>
</html>
```